Business Card Design Project

We are after a business card design for our construction company. Called R & T Holloway Construction Solutions. We build designer homes mainly one of's. We would like something with punch, eye catching like the homes we build, modern style maybe geometrical or slightly abstract. It is a long business name we realise but we wont mind if our name is more in the back ground making Construction Solutions the focus ??? Colours maybe purple and black ??? Don't really have any set colours.

Industry/Entity Type

Construction

Requirements
Must have
• Business name contact details and our personal names perhaps at bottom somewhere
Nice to have
• A business card which has a simple easily recognised symbol or logo on it

```html
<!DOCTYPE html>
<html lang="en">
<head>
<meta charset="utf-8">
<title>R &amp; T Holloway Construction Solutions – Business Card</title>
<link rel="stylesheet" href="https://fonts.googleapis.com/css2?family=Questrial&display=swap">
<style>
  :root {
    --paper: #ffffff;
    --card-black: #000000;
    --brand-purple: #7a12e6;
    --brand-magenta: #cc00ff;
    --ink-white: #ffffff;
    --ink-dark: #111111;
    --swatch-border: #333333;
  }
  * { margin: 0; padding: 0; box-sizing: border-box; }
  html, body {
    width: 1200px;
    height: 848px;
    overflow: hidden;
    background: var(--paper);
    font-family: "Questrial", "Century Gothic", sans-serif;
  }
  .canvas { position: relative; width: 1200px; height: 848px; }

  .business-card {
    position: absolute;
    left: 87px; top: 180px;
    width: 777px; height: 442px;
    background: var(--card-black);
    color: var(--ink-white);
  }
  .card-divider {
    position: absolute;
    left: 389px; top: 30px;
    width: 3px; height: 430px;
    background: linear-gradient(to bottom, rgba(122,18,230,0) 0%, rgba(122,18,230,0.9) 45%, rgba(122,18,230,0.6) 85%, rgba(122,18,230,0) 100%);
  }

  .brand-block {
    position: absolute;
    left: 20px; top: 150px;
    width: 350px;
    text-align: center;
    color: var(--brand-purple);
    font-size: 31px;
    line-height: 1.35;
    letter-spacing: -0.5px;
  }

  .owner-names {
    position: absolute;
    left: 440px; top: 80px;
    color: var(--brand-purple);
    font-size: 25px;
  }
  .owner-role {
    position: absolute;
    left: 441px; top: 109px;
    font-size: 13px;
  }
  .contact-address, .contact-lines {
    position: absolute;
    right: 34px;
    text-align: right;
    font-size: 16.5px;
    line-height: 20.5px;
  }
  .contact-address { top: 214px; }
  .contact-lines { top: 296px; }
  .licence {
    position: absolute;
    right: 34px; top: 409px;
    font-size: 12.5px;
  }

  .colour-legend {
    position: absolute;
    left: 924px; top: 243px;
    color: var(--ink-dark);
    font-size: 15px;
  }
  .legend-title { margin-bottom: 20px; }
  .swatch-row { display: flex; align-items: center; height: 43px; }
  .swatch {
    width: 29px; height: 29px;
    border: 1.5px solid var(--swatch-border);
    margin-right: 12px;
  }
  .swatch--white { background: var(--ink-white); }
  .swatch--purple { background: var(--brand-purple); }
  .swatch--black { background: var(--card-black); }
  .swatch--magenta { background: var(--brand-magenta); }
  .font-notes { margin-top: 42px; line-height: 19px; }
  .font-notes .indent { padding-left: 42px; }
</style>
</head>
<body>
<div class="canvas">
  <section class="business-card">
    <div class="brand-block">
      <div>R &amp; T Holloway</div>
      <div>Construction Solutions</div>
    </div>

    <div class="card-divider"></div>

    <div class="owner-names">Ross &amp; Tina Holloway</div>
    <div class="owner-role">Builders</div>

    <address class="contact-address" style="font-style:normal">
      12 Marlow Street<br>
      Ravenswood Ridge<br>
      QLD 4821
    </address>

    <div class="contact-lines">
      Email:- rtholloway@stonemail.net.au<br>
      Phone 0491 570156 or 04915701100
    </div>

    <div class="licence">BSA License - 1093275</div>
  </section>

  <aside class="colour-legend">
    <div class="legend-title">Pantone Colors</div>
    <div class="swatch-row"><span class="swatch swatch--white"></span>White</div>
    <div class="swatch-row"><span class="swatch swatch--purple"></span>Process 172-1 C</div>
    <div class="swatch-row"><span class="swatch swatch--black"></span>Black</div>
    <div class="swatch-row"><span class="swatch swatch--magenta"></span>Pantone DS 164 - 1 C</div>
    <div class="font-notes">
      <div>Fonts - AvantGarde Md BT</div>
      <div class="indent">- AvantGarde Bk BT</div>
    </div>
  </aside>
</div>
</body>
</html>
```